Mission statement design for a secondary school

We have the content of our mission statement and need an appealing layout. The design should fit on a poster or A4 page. The content grouping in the document should also be graphically recognizable. Our target group are young people and their parents as well as the school staff, which is why we need a modern design that is not out after 2 years. It must be easy to grasp visually and graphically simple.

Target Market(s)

Actors of the school

Requirements
Must have
• cantonal logo including school name see document can be integrated as a header
Should not have
• References to trademarks or third parties

```html
<!DOCTYPE html>
<html lang="de">
<head>
<meta charset="utf-8">
<title>Leitbild – Sekundarschule Lindenau</title>
<link rel="stylesheet" href="https://fonts.googleapis.com/css2?family=Barlow:wght@300;400;600;700&family=Barlow+Condensed:wght@600;700&display=swap">
<style>
:root{
  --stage:#666666;
  --paper:#ffffff;
  --red:#ff0000;
  --dark:#333333;
  --black:#1c1c1c;
  --panel:#ebebeb;
  --panel-soft:#f2f2f2;
  --ghost:#e6e6e6;
  --text:#2b2b2b;
}
*{margin:0;padding:0;box-sizing:border-box}
html,body{width:1200px;height:817px;overflow:hidden;background:var(--stage);font-family:"Barlow",sans-serif}
.sample-label{position:absolute;top:15px;color:#fff;font-size:15px;font-weight:400}
.poster{position:absolute;top:45px;width:1001px;height:1419px;background:var(--paper);transform-origin:0 0;transform:scale(.5163);overflow:hidden;box-shadow:0 4px 18px rgba(0,0,0,.35)}
.watermark{position:absolute;left:36px;top:1300px;width:1260px;height:140px;transform-origin:0 0;transform:rotate(-90deg);font-weight:700;font-size:176px;line-height:140px;color:var(--ghost);white-space:nowrap;letter-spacing:2px}
.deco-x{position:absolute;left:0;top:0}
.brand{position:absolute;right:64px;top:26px;text-align:right;color:var(--red)}
.brand-name{font-weight:600;font-size:52px;line-height:48px;letter-spacing:5px;display:flex;align-items:center;justify-content:flex-end;gap:16px}
.brand-mark{width:26px;height:26px;background:var(--red)}
.brand-sub{font-weight:700;font-size:15.5px;line-height:20px;letter-spacing:1px;margin-top:18px}
.banner{position:absolute;left:0;top:183px;width:1001px;height:122px}
.banner-text{position:absolute;left:358px;top:196px;color:#fff;font-size:29px;line-height:32px;font-weight:400}
.banner-text strong{font-weight:600}
.bar{position:absolute;height:40px;color:#fff;font-family:"Barlow Condensed",sans-serif;font-weight:700;font-size:36px;line-height:40px;padding-left:30px}
.bar.red{background:var(--red)}
.bar.dark{background:var(--dark)}
.badge{position:absolute;border-radius:50%;background:#fff;display:flex;align-items:center;justify-content:center}
.badge.red{border:5px solid var(--red)}
.badge.darkring{border:5px solid var(--dark)}
.panel{position:absolute;background:var(--panel)}
.lead{position:absolute;font-family:"Barlow Condensed",sans-serif;font-weight:700;color:var(--text)}
.checks{position:absolute;list-style:none;color:var(--text);font-weight:400}
.checks li{position:relative;padding-left:28px}
.checks li::before{content:"✓";position:absolute;left:0;top:0;color:var(--red);font-weight:700;font-size:.8em}
.s1-haltung{font-size:19.5px;line-height:25px;width:330px}
.s1-haltung li{margin-bottom:6px}
.s1-small{font-size:16.5px;line-height:23px;width:320px;font-weight:300}
.s1-small li{margin-bottom:6px}
.s1-gem{font-size:19px;line-height:25px;width:340px}
.s1-gem li{margin-bottom:8px}
.s2-list{font-size:18px;line-height:25.2px;width:720px}
.footer{position:absolute;left:0;top:1327px;width:1001px;height:92px}
.footer-text{position:absolute;left:0;width:1001px;top:1336px;text-align:center;color:#fff;font-family:"Barlow Condensed",sans-serif;font-weight:700;font-size:22px;line-height:26px}
</style>
</head>
<body>

<div class="sample-label" style="left:45px">Sample 1</div>
<div class="sample-label" style="left:638px">Sample 2</div>

<!-- ============ Layout A: two columns ============ -->
<section class="poster" style="left:45px">
  <svg class="deco-x" width="1001" height="200" viewBox="0 0 1001 200">
    <polygon points="320,0 400,0 210,200 130,200" fill="#e9e9e9"/>
    <polygon points="410,0 500,0 690,200 600,200" fill="#f1f1f1"/>
  </svg>
  <div class="watermark">UNSER LEITBILD</div>

  <div class="brand">
    <div class="brand-name">KANTON<span class="brand-mark"></span></div>
    <div class="brand-name" style="padding-right:42px">TALHEIM</div>
    <div class="brand-sub">BILDUNGS-, KULTUR- UND SPORTDIREKTION<br>SEKUNDARSCHULE LINDENAU</div>
  </div>

  <svg class="banner" viewBox="0 0 1001 122">
    <rect x="205" y="0" width="8" height="122" fill="var(--red)"/>
    <rect x="220" y="0" width="781" height="122" fill="var(--dark)"/>
    <polygon points="900,0 988,0 895,122 825,122" fill="var(--red)"/>
    <polygon points="950,60 1001,122 905,122" fill="#444"/>
    <g fill="none" stroke="var(--red)" stroke-width="3">
      <rect x="258" y="38" width="62" height="52"/>
      <line x1="289" y1="38" x2="289" y2="90"/>
      <polyline points="230,80 245,74 255,82"/>
      <polyline points="320,60 338,52"/>
    </g>
  </svg>
  <div class="banner-text">Es gibt drei Kategorien<br><strong>(Lernen, Entwicklung, Gemeinschaft)</strong><br>und die Haltung der Schule.</div>

  <!-- Haltung -->
  <div class="bar red" style="left:290px;top:362px;width:320px">HALTUNG</div>
  <div class="badge red" style="left:204px;top:330px;width:110px;height:110px">
    <svg width="50" height="50" viewBox="0 0 50 50" fill="none" stroke="#333" stroke-width="2.5"><circle cx="25" cy="22" r="14"/><line x1="25" y1="16" x2="25" y2="28"/><line x1="19" y1="22" x2="31" y2="22"/><line x1="20" y1="36" x2="20" y2="46"/></svg>
  </div>
  <div class="lead" style="left:328px;top:412px;font-size:29px">An unserer Schule...</div>
  <ul class="checks s1-haltung" style="left:236px;top:474px">
    <li>stehen die Lernenden im Mittelpunkt.</li>
    <li>ist Integration selbstverständlich.</li>
    <li>begegnen wir uns respektvoll und wertschätzend.</li>
    <li>setzen wir uns für lebenslanges Lernen ein.</li>
  </ul>

  <!-- Entwicklung -->
  <div class="panel" style="left:600px;top:360px;width:375px;height:440px;border-radius:0 0 18px 0"></div>
  <div class="bar dark" style="left:650px;top:360px;width:351px;padding-left:80px">ENTWICKLUNG</div>
  <div class="badge darkring" style="left:598px;top:328px;width:106px;height:106px">
    <svg width="50" height="50" viewBox="0 0 50 50" fill="none" stroke="var(--red)" stroke-width="2.5"><circle cx="25" cy="25" r="7"/><circle cx="25" cy="25" r="13"/><rect x="4" y="4" width="9" height="9"/><rect x="37" y="37" width="9" height="9"/></svg>
  </div>
  <ul class="checks s1-small" style="left:622px;top:438px">
    <li>Wir entwickeln unsere Schule gemeinsam.</li>
    <li>Wir setzen unsere Fähigkeiten und Kräfte gezielt ein.</li>
    <li>Alle tragen Verantwortung.</li>
    <li>Wir lernen alle voneinander.</li>
    <li>Wir bilden uns kontinuierlich weiter.</li>
    <li>Wir reflektieren unser Handeln.</li>
    <li>Wir sind innovativ und gehen mutig unseren Weg.</li>
  </ul>

  <!-- Lernen -->
  <div class="panel" style="left:197px;top:830px;width:373px;height:470px;border-radius:0 0 18px 18px"></div>
  <div class="bar dark" style="left:280px;top:786px;width:320px;padding-left:45px">LERNEN</div>
  <div class="badge darkring" style="left:199px;top:754px;width:108px;height:108px">
    <svg width="54" height="50" viewBox="0 0 54 50" fill="none" stroke="var(--red)" stroke-width="2.5"><path d="M4 8 L27 4 L27 46 L4 46 Z"/><path d="M50 8 L27 4 L27 46 L50 46 Z"/><line x1="10" y1="18" x2="22" y2="16"/><line x1="10" y1="26" x2="22" y2="24"/><line x1="10" y1="34" x2="22" y2="32"/><line x1="32" y1="16" x2="44" y2="18"/><line x1="32" y1="24" x2="44" y2="26"/><line x1="32" y1="32" x2="44" y2="34"/></svg>
  </div>
  <ul class="checks s1-small" style="left:225px;top:874px">
    <li>Wir begleiten unsere Lernendenhin zur Selbständigkeit.</li>
    <li>Wir unterstützen unsere Lernenden in ihrem individuellen Kompetenzer­werb.</li>
    <li>Wir ermöglichen allen Lernenden Erfolge.</li>
    <li>Die Unterrichtsinhalte orientieren sich an aktuellen Themen.</li>
    <li>Wir beurteilen transparent.</li>
    <li>Wir begegnen Heterogenität mit multiprofessionellen Teams.</li>
    <li>Wir schaffen eine wertschätzende und förderliche Atmosphäre.</li>
    <li>Unsere Schule bietet eine zeitgemässe Infrastruktur.</li>
  </ul>

  <!-- Gemeinschaft -->
  <div class="bar red" style="left:680px;top:782px;width:321px;padding-left:33px">GEMEINSCHAFT</div>
  <div class="badge red" style="left:589px;top:749px;width:108px;height:108px">
    <svg width="52" height="52" viewBox="0 0 52 52" fill="none" stroke="#333" stroke-width="2.5"><circle cx="10" cy="10" r="6"/><circle cx="42" cy="10" r="6"/><circle cx="10" cy="42" r="6"/><circle cx="42" cy="42" r="6"/><circle cx="26" cy="26" r="6" stroke="var(--red)"/><line x1="15" y1="15" x2="21" y2="21"/><line x1="37" y1="15" x2="31" y2="21"/><line x1="15" y1="37" x2="21" y2="31"/><line x1="37" y1="37" x2="31" y2="31"/></svg>
  </div>
  <ul class="checks s1-gem" style="left:615px;top:874px">
    <li>Unsere Schule achtet die Gesundheit aller.</li>
    <li>Wir legen Wert auf eine offene Kommunikation.</li>
    <li>Unsere pädagogische Zusammenar­beit basiert auf einer professionellen Haltung.</li>
    <li>Die Eltern sind ein Teil unserer Schulgemeinschaft und tragen Verantwortung.</li>
    <li>Wir haben an unserer Schule Freiräume innerhalb klarer Rahmenbedingungen.</li>
  </ul>

  <svg class="footer" viewBox="0 0 1001 92">
    <rect x="0" y="0" width="1001" height="92" fill="var(--black)"/>
    <rect x="0" y="0" width="1001" height="8" fill="var(--red)"/>
    <polygon points="205,0 796,0 740,72 250,72" fill="var(--red)"/>
    <polyline points="0,20 205,20 255,80" fill="none" stroke="var(--red)" stroke-width="2"/>
    <polyline points="1001,20 796,20 746,80" fill="none" stroke="var(--red)" stroke-width="2"/>
  </svg>
  <div class="footer-text">Sekundarschule Lindenau, Birkenweg 12, 4100 Lindenau<br>061 000 12 34&nbsp; | &nbsp;sekundarschule.lindenau@schulnetz.ch</div>
</section>

<!-- ============ Layout B: stacked ============ -->
<section class="poster" style="left:638px">
  <svg class="deco-x" width="1001" height="200" viewBox="0 0 1001 200">
    <polygon points="320,0 400,0 210,200 130,200" fill="#e9e9e9"/>
    <polygon points="410,0 500,0 690,200 600,200" fill="#f1f1f1"/>
  </svg>
  <div class="watermark">UNSER LEITBILD</div>

  <div class="brand">
    <div class="brand-name">KANTON<span class="brand-mark"></span></div>
    <div class="brand-name" style="padding-right:42px">TALHEIM</div>
    <div class="brand-sub">BILDUNGS-, KULTUR- UND SPORTDIREKTION<br>SEKUNDARSCHULE LINDENAU</div>
  </div>

  <svg class="banner" viewBox="0 0 1001 122">
    <rect x="205" y="0" width="8" height="122" fill="var(--red)"/>
    <rect x="220" y="0" width="781" height="122" fill="var(--dark)"/>
    <polygon points="900,0 988,0 895,122 825,122" fill="var(--red)"/>
    <polygon points="950,60 1001,122 905,122" fill="#444"/>
    <g fill="none" stroke="var(--red)" stroke-width="3">
      <rect x="258" y="38" width="62" height="52"/>
      <line x1="289" y1="38" x2="289" y2="90"/>
      <polyline points="230,80 245,74 255,82"/>
      <polyline points="320,60 338,52"/>
    </g>
  </svg>
  <div class="banner-text">Es gibt drei Kategorien<br><strong>(Lernen, Entwicklung, Gemeinschaft)</strong><br>und die Haltung der Schule.</div>

  <!-- Haltung -->
  <svg style="position:absolute;left:230px;top:347px" width="520" height="40" viewBox="0 0 520 40">
    <polygon points="0,0 215,0 215,40 0,40" fill="var(--red)"/>
    <polygon points="205,0 505,0 515,40 215,40" fill="var(--dark)"/>
  </svg>
  <div class="lead" style="left:280px;top:348px;font-size:35px;color:#fff;line-height:40px">HALTUNG</div>
  <div class="lead" style="left:468px;top:348px;font-size:31px;color:#fff;line-height:40px">An unserer Schule...</div>
  <div class="badge red" style="left:205px;top:332px;width:66px;height:66px"><svg width="32" height="32" viewBox="0 0 50 50" fill="none" stroke="#333" stroke-width="3"><circle cx="25" cy="22" r="14"/><line x1="25" y1="16" x2="25" y2="28"/><line x1="19" y1="22" x2="31" y2="22"/></svg></div>
  <ul class="checks s2-list" style="left:268px;top:402px">
    <li>stehen die Lernenden im Mittelpunkt.</li>
    <li>ist Integration selbstverständlich.</li>
    <li>begegnen wir uns respektvoll und wertschätzend.</li>
    <li>setzen wir uns für lebenslanges Lernen ein.</li>
  </ul>

  <!-- Lernen -->
  <div class="panel" style="left:237px;top:545px;width:764px;height:267px;background:var(--panel-soft);border-radius:0 0 0 20px"></div>
  <svg style="position:absolute;left:230px;top:530px" width="230" height="40"><polygon points="0,0 215,0 225,40 0,40" fill="var(--red)"/></svg>
  <div class="lead" style="left:280px;top:530px;font-size:35px;color:#fff;line-height:40px">LERNEN</div>
  <div class="badge red" style="left:205px;top:515px;width:66px;height:66px"><svg width="32" height="30" viewBox="0 0 54 50" fill="none" stroke="#333" stroke-width="3"><path d="M4 8 L27 4 L27 46 L4 46 Z"/><path d="M50 8 L27 4 L27 46 L50 46 Z"/></svg></div>
  <ul class="checks s2-list" style="left:268px;top:590px">
    <li>Wir begleiten unsere Lernendenhin zur Selbständigkeit.</li>
    <li>Wir unterstützen unsere Lernenden in ihrem individuellen Kompetenzerwerb.</li>
    <li>Wir ermöglichen allen Lernenden Erfolge.</li>
    <li>Die Unterrichtsinhalte orientieren sich an aktuellen Themen.</li>
    <li>Wir beurteilen transparent.</li>
    <li>Wir begegnen Heterogenität mit multiprofessionellen Teams.</li>
    <li>Wir schaffen eine wertschätzende und förderliche Atmosphäre.</li>
    <li>Unsere Schule bietet eine zeitgemässe Infrastruktur.</li>
  </ul>

  <!-- Entwicklung -->
  <svg style="position:absolute;left:230px;top:848px" width="330" height="40"><polygon points="0,0 310,0 320,40 0,40" fill="var(--red)"/></svg>
  <div class="lead" style="left:287px;top:848px;font-size:35px;color:#fff;line-height:40px">ENTWICKLUNG</div>
  <div class="badge red" style="left:205px;top:833px;width:66px;height:66px"><svg width="32" height="32" viewBox="0 0 50 50" fill="none" stroke="#333" stroke-width="3"><circle cx="25" cy="25" r="7"/><circle cx="25" cy="25" r="13"/></svg></div>
  <ul class="checks s2-list" style="left:268px;top:898px">
    <li>Wir entwickeln unsere Schule gemeinsam.</li>
    <li>Wir setzen unsere Fähigkeiten und Kräfte gezielt ein.</li>
    <li>Alle tragen Verantwortung.</li>
    <li>Wir lernen alle voneinander.</li>
    <li>Wir bilden uns kontinuierlich weiter.</li>
    <li>Wir reflektieren unser Handeln.</li>
    <li>Wir sind innovativ und gehen mutig unseren Weg.</li>
  </ul>

  <!-- Gemeinschaft -->
  <div class="panel" style="left:237px;top:1120px;width:764px;height:180px;background:var(--panel-soft);border-radius:0 0 0 20px"></div>
  <svg style="position:absolute;left:230px;top:1103px" width="350" height="40"><polygon points="0,0 330,0 340,40 0,40" fill="var(--red)"/></svg>
  <div class="lead" style="left:285px;top:1103px;font-size:35px;color:#fff;line-height:40px">GEMEINSCHAFT</div>
  <div class="badge red" style="left:205px;top:1088px;width:66px;height:66px"><svg width="34" height="34" viewBox="0 0 52 52" fill="none" stroke="#333" stroke-width="3"><circle cx="10" cy="10" r="6"/><circle cx="42" cy="10" r="6"/><circle cx="10" cy="42" r="6"/><circle cx="42" cy="42" r="6"/><circle cx="26" cy="26" r="6"/></svg></div>
  <ul class="checks s2-list" style="left:268px;top:1154px;width:720px">
    <li>Unsere Schule achtet die Gesundheit aller.</li>
    <li>Wir legen Wert auf eine offene Kommunikation.</li>
    <li>Unsere pädagogische Zusammenarbeit basiert auf einer professionellen Haltung.</li>
    <li>Die Eltern sind ein Teil unserer Schulgemeinschaft und tragen Verantwortung.</li>
    <li>Wir haben an unserer Schule Freiräume innerhalb klarer Rahmenbedingungen.</li>
  </ul>

  <svg class="footer" viewBox="0 0 1001 92">
    <rect x="0" y="0" width="1001" height="92" fill="var(--black)"/>
    <rect x="0" y="0" width="1001" height="8" fill="var(--red)"/>
    <polygon points="205,0 796,0 740,72 250,72" fill="var(--red)"/>
    <polyline points="0,20 205,20 255,80" fill="none" stroke="var(--red)" stroke-width="2"/>
    <polyline points="1001,20 796,20 746,80" fill="none" stroke="var(--red)" stroke-width="2"/>
  </svg>
  <div class="footer-text">Sekundarschule Lindenau, Birkenweg 12, 4100 Lindenau<br>061 000 12 34&nbsp; | &nbsp;sekundarschule.lindenau@schulnetz.ch</div>
</section>

</body>
</html>
```